Flyer Design

We are a new charity. Our immediate aim is to respond to the ebola crisis in Sierra Leone. We need a flier or a booklet to inform and raise funds.

Industry/Entity Type

Charity

Requirements
Must have
• The donation page and the gift aid form should be at the back and in a back and front format.
Nice to have
• Front page with our best photo

```html
<!DOCTYPE html>
<html lang="en">
<head>
<meta charset="utf-8">
<title>Gift Aid Declaration Flyer</title>
<link href="https://fonts.googleapis.com/css2?family=Source+Sans+3:wght@400;600;700&display=swap" rel="stylesheet">
<style>
  :root {
    --stage: #8a8a8a;
    --brand-blue: #22a0dc;
    --paper: #ffffff;
    --ink: #2b2b2b;
    --rule: #7a7a7a;
    --photo-top: #4f6b3c;
    --photo-mid: #8a7a63;
    --photo-low: #b9ab94;
  }
  * { box-sizing: border-box; margin: 0; padding: 0; }
  html, body {
    width: 1200px; height: 900px; overflow: hidden;
    background: var(--stage);
    font-family: "Source Sans 3", "Myriad Pro", Arial, sans-serif;
    color: var(--ink);
  }
  .flyer {
    position: absolute; left: 290px; top: 18px;
    width: 620px; height: 864px;
    background: var(--brand-blue);
    padding: 44px 22px 22px;
  }
  .flyer__title {
    position: absolute; top: 12px; left: 0; right: 0;
    text-align: center; color: var(--paper);
    font-weight: 700; font-size: 15px; letter-spacing: 0.4px;
  }
  .flyer__panel {
    position: relative; height: 100%;
    background: var(--paper); border-radius: 22px;
    padding: 18px 24px 18px; overflow: hidden;
  }
  .form { position: relative; font-size: 10.5px; line-height: 1.35; }
  .form p { margin-bottom: 6px; }
  .form strong { font-weight: 700; }
  .field { display: flex; gap: 6px; align-items: flex-end; margin-bottom: 7px; }
  .field__line { flex: 1; border-bottom: 1px solid var(--rule); height: 11px; }
  .field__line--short { flex: 0 0 70px; }
  .photo {
    position: absolute; left: 14px; right: 14px; bottom: 14px; height: 410px;
    border-radius: 18px;
    background: linear-gradient(180deg, var(--photo-top) 0%, var(--photo-mid) 45%, var(--photo-low) 100%);
  }
</style>
</head>
<body>
  <article class="flyer">
    <h1 class="flyer__title">GIFT AID DECLARATION – FOR PAST, PRESENT &amp; FUTURE DONATIONS</h1>
    <div class="flyer__panel">
      <form class="form">
        <div class="field"><span>Name of charity or Community Amateur Sports Club</span><span class="field__line"></span></div>
        <p><strong>PLEASE TREAT AS GIFT AID DONATIONS ALL QUALIFYING GIFTS OF MONEY MADE</strong></p>
        <div class="field">
          <span>today</span><span class="field__line field__line--short"></span>
          <span>in the past 4 years</span><span class="field__line field__line--short"></span>
          <span>in the future</span><span class="field__line"></span>
        </div>
        <p>Please tick all boxes you wish to apply.</p>
        <p>I confirm I have paid or will pay an amount of Income Tax and/or Capital Gains Tax for each tax year (6 April to 5 April) that is at least equal to the amount of tax that all the charities or Community Amateur Sports Clubs (CASCs) that I donate to will reclaim on my gifts for that tax year. I understand that other taxes such as VAT and Council Tax do not qualify. I understand the charity will reclaim 28p of tax on every £1 that I gave up to 5 April 2008 and will reclaim 25p of tax on every £1 that I give on or after 6 April 2008.</p>
        <p>Donor’s details</p>
        <div class="field">
          <span>Title</span><span class="field__line field__line--short"></span>
          <span>First name or initial(s)</span><span class="field__line"></span>
          <span>Surname</span><span class="field__line"></span>
        </div>
        <div class="field"><span>Full home address</span><span class="field__line"></span></div>
        <div class="field">
          <span class="field__line"></span><span>Postcode</span><span class="field__line field__line--short"></span>
        </div>
        <div class="field">
          <span>Date</span><span class="field__line"></span>
          <span>Signature</span><span class="field__line"></span>
        </div>
        <p>Please notify the charity or CASC if you: Want to cancel this declaration | Change your name or home address | No longer pay sufficient tax on your income and/or capital gains.</p>
        <p>If you pay Income Tax at the higher or additional rate and want to receive the additional tax relief due to you, you must include all your Gift Aid donations on your Self Assessment tax return or ask HM Revenue and Customs to adjust your tax code.</p>
      </form>

      <div class="photo" role="img" aria-label="Photograph of a large group of village children standing together outside a small building, with trees behind them"></div>
    </div>
  </article>
</body>
</html>
```